Branding Design for KQ-Reef’s Exterior & Fleet

About Us
KQ-Reef is a NEMO-certified dive center on the island of Bonaire, known worldwide for its high diving standards. We specialize in Unlimited Air diving and offer a unique experience for divers with our Unlimited Air per day and Tank Cards. We offer the lowest price guarantee
What We Need
We are launching a design contest to create high-impact branding visuals for the exterior of our office and our pickup truck fleet, ensuring maximum visibility for our Unlimited Air service.
Design Locations:
1. Wall & Small Building at Our Z-7 Office Location (see attached pictures and sizes (7.50 meters x 2 + 2.1 meters hight) width , the lower part 2 meter high are cars parked,so is not really usefull. )
o A striking, high-visibility design promoting Unlimited Air & Tank Cards.
o The design must be clear, bold, and immediately recognizable for passing traffic.
2. Pickup Truck Tailgate Stickers (Fleet of 150)
o A concise, attention-grabbing design that promotes Unlimited Air and tnak cards.
o Needs to be easily understood in seconds as people drive past.

Key Messages to Include:
✔ Unlimited Air – No restrictions, dive freely!
✔ Tank Cards – Easy, flexible, and cost-effective.
✔ Lowest Price Guarantee – Best deal on the island!
✔ NEMO Certified – A globally recognized diving standard.
Design Guidelines:
🎨 Incorporate the NEMO Logo – NEMO is a worldwide brand, making us instantly recognizable.
🎨 Use NEMO Colors – The color scheme should align with NEMO branding while maintaining a balance with KQ-Reef’s identity.
🎨 Include the KQ-Reef Logo – It must be present but should not overpower the design.
🎨 Simple & Bold – The message must be understood at a glance.
🎨 Bonaire Vibes – Use ocean-inspired elements reflecting diving culture.
🎨 Professional & Premium – KQ-Reef is a trusted, high-quality dive center.
Submission Details:
• Designs must be in high-resolution formats (AI, PSD, PDF, or PNG).
• Ensure the design can be scaled for different placements.
• The winning design will be featured prominently on Bonaire, seen by thousands of divers and tourists daily!
We look forward to your creative ideas—good luck!

```html
<!DOCTYPE html>
<html lang="en">
<head>
<meta charset="utf-8">
<title>KQ-Reef Exterior &amp; Fleet Branding</title>
<link rel="stylesheet" href="https://fonts.googleapis.com/css2?family=Exo+2:ital,wght@1,800;1,900&family=Titillium+Web:ital,wght@0,700;1,700&display=swap">
<style>
  :root {
    --navy: #2e3860;
    --sky: #72cdf4;
    --orange: #f7a836;
    --white: #ffffff;
    --sea-deep: #1d4f9a;
    --sea-mid: #3d86b8;
    --reef: #b88a3a;
  }
  html, body { margin: 0; padding: 0; width: 960px; height: 1200px; overflow: hidden; background: var(--white); }
  .board { display: block; width: 960px; height: 1200px; }
  .label { font-family: "Titillium Web", sans-serif; font-style: italic; font-weight: 700; fill: var(--navy); }
  .headline { font-family: "Exo 2", sans-serif; font-style: italic; font-weight: 900; }
  .on-navy { fill: var(--white); }
  .accent { fill: var(--sky); }
  .offer-title { font-family: "Titillium Web", sans-serif; font-style: italic; font-weight: 700; fill: var(--navy); }
  .offer-sub { font-family: "Titillium Web", sans-serif; font-style: italic; font-weight: 700; fill: var(--white); }
  .brand-name { font-family: "Titillium Web", sans-serif; font-weight: 700; fill: var(--navy); }
  .web { font-family: "Titillium Web", sans-serif; font-style: italic; font-weight: 700; }
  .navy-fill { fill: var(--navy); }
  .sky-fill { fill: var(--sky); }
  .white-fill { fill: var(--white); }
  .orange-fill { fill: var(--orange); }
  .globe { fill: none; stroke-width: 2.5; }
</style>
</head>
<body>
<svg class="board" viewBox="0 0 1732 2165" xmlns="http://www.w3.org/2000/svg">
  <defs>
    <linearGradient id="sea-turtle" x1="0" y1="0" x2="0" y2="1">
      <stop offset="0" stop-color="#3f8fc4"/><stop offset="1" stop-color="#1a3f9a"/>
    </linearGradient>
    <linearGradient id="sea-divers" x1="0" y1="0" x2="0" y2="1">
      <stop offset="0" stop-color="#4aa6d6"/><stop offset="0.7" stop-color="#2f6e9e"/><stop offset="1" stop-color="#a5813a"/>
    </linearGradient>
    <linearGradient id="sea-angelfish" x1="0" y1="0" x2="1" y2="1">
      <stop offset="0" stop-color="#3a3a36"/><stop offset="0.5" stop-color="#6a9a7a"/><stop offset="1" stop-color="#2a2a2a"/>
    </linearGradient>
    <linearGradient id="sea-barracuda" x1="0" y1="0" x2="0" y2="1">
      <stop offset="0" stop-color="#4aa1b4"/><stop offset="1" stop-color="#c98f6a"/>
    </linearGradient>
    <linearGradient id="sea-open" x1="0" y1="0" x2="0" y2="1">
      <stop offset="0" stop-color="#2f78b8"/><stop offset="1" stop-color="#5aa4c8"/>
    </linearGradient>
  </defs>

  <!-- Section labels -->
  <text class="label" x="1240" y="195" font-size="32">Wall</text>
  <text class="label" x="1240" y="898" font-size="32">Office</text>
  <text class="label" x="1240" y="1857" font-size="32">Pickup Truck Tailgate Stickers</text>

  <!-- Wall banner: Enjoy the waters -->
  <g class="wall-banner">
    <rect class="navy-fill" x="41" y="254" width="809" height="453"/>
    <polygon class="sky-fill" points="468,254 850,254 850,707 268,707"/>
    <polygon class="white-fill" points="118,254 287,254 287,380 203,415 118,380"/>
    <text class="brand-name" x="203" y="360" font-size="36" text-anchor="middle">KQ-Reef</text>
    <g class="partner-mark">
      <circle class="navy-fill" cx="787" cy="285" r="20"/>
      <text class="brand-name" x="787" y="324" font-size="20" text-anchor="middle">NEMO</text>
    </g>
    <text class="headline on-navy" x="78" y="453" font-size="44" textLength="272">ENJOY THE</text>
    <text class="headline" x="70" y="494" font-size="44"><tspan class="on-navy">WATERS</tspan><tspan class="accent"> OF</tspan></text>
    <text class="headline accent" x="66" y="534" font-size="44" textLength="232">BONAIRE</text>
    <rect class="orange-fill" x="387" y="333" width="424" height="107" rx="12"/>
    <text class="offer-title" x="599" y="396" font-size="72" text-anchor="middle" textLength="400">Unlimited Air</text>
    <text class="offer-sub" x="599" y="429" font-size="31" text-anchor="middle" textLength="365">No restrictions, dive freely!</text>
    <rect class="orange-fill" x="387" y="494" width="424" height="107" rx="12"/>
    <text class="offer-title" x="596" y="558" font-size="72" text-anchor="middle" textLength="332">Tank Cards</text>
    <text class="offer-sub" x="599" y="590" font-size="29" text-anchor="middle" textLength="402">Easy, flexible, and cost-effective.</text>
    <g class="web-address">
      <circle class="globe" cx="80" cy="665" r="10" stroke="var(--sky)"/>
      <line x1="70" y1="665" x2="90" y2="665" stroke="var(--sky)" stroke-width="2"/>
      <ellipse class="globe" cx="80" cy="665" rx="4" ry="10" stroke="var(--sky)" stroke-width="2"/>
      <text class="web on-navy" x="97" y="675" font-size="32">kq-reef.com</text>
    </g>
    <g role="img" aria-label="Underwater photo of a sea turtle">
      <polygon points="314,604 433,604 433,707 268,707" fill="url(#sea-turtle)"/>
    </g>
    <g role="img" aria-label="Underwater photo of divers over coral">
      <rect x="433" y="604" width="119" height="103" fill="url(#sea-divers)"/>
    </g>
    <g role="img" aria-label="Photo of a queen angelfish on the reef">
      <rect x="552" y="604" width="150" height="103" fill="url(#sea-angelfish)"/>
    </g>
    <g role="img" aria-label="Photo of a barracuda above brain coral">
      <rect x="702" y="604" width="148" height="103" fill="url(#sea-barracuda)"/>
    </g>
  </g>

  <!-- Wall banner: Discover scuba diving -->
  <g class="wall-banner">
    <rect class="navy-fill" x="876" y="254" width="809" height="453"/>
    <polygon class="sky-fill" points="1303,254 1685,254 1685,707 1105,707"/>
    <polygon class="white-fill" points="960,254 1128,254 1128,380 1044,415 960,380"/>
    <text class="brand-name" x="1044" y="360" font-size="36" text-anchor="middle">KQ-Reef</text>
    <g class="partner-mark">
      <circle class="navy-fill" cx="1625" cy="285" r="20"/>
      <text class="brand-name" x="1625" y="324" font-size="20" text-anchor="middle">NEMO</text>
    </g>
    <text class="headline on-navy" x="902" y="453" font-size="44" textLength="250">DISCOVER</text>
    <text class="headline accent" x="900" y="494" font-size="44" textLength="172">SCUBA</text>
    <text class="headline on-navy" x="900" y="534" font-size="44" textLength="178">DIVING</text>
    <rect class="orange-fill" x="1222" y="333" width="424" height="107" rx="12"/>
    <text class="offer-title" x="1420" y="398" font-size="72" text-anchor="middle" textLength="378">Lowest Price</text>
    <text class="offer-sub" x="1410" y="429" font-size="31" text-anchor="middle" textLength="316">Best deal on the island!</text>
    <rect class="orange-fill" x="1222" y="494" width="424" height="107" rx="12"/>
    <text class="offer-title" x="1434" y="558" font-size="68" text-anchor="middle" textLength="402">NEMO Certified</text>
    <text class="offer-sub" x="1436" y="593" font-size="25" text-anchor="middle" textLength="396">A globally recognized diving standard.</text>
    <g class="web-address">
      <circle class="globe" cx="905" cy="665" r="10" stroke="var(--sky)"/>
      <line x1="895" y1="665" x2="915" y2="665" stroke="var(--sky)" stroke-width="2"/>
      <ellipse class="globe" cx="905" cy="665" rx="4" ry="10" stroke="var(--sky)" stroke-width="2"/>
      <text class="web on-navy" x="922" y="675" font-size="32">kq-reef.com</text>
    </g>
    <g role="img" aria-label="Underwater photo of a squid">
      <polygon points="1151,602 1240,602 1240,707 1105,707" fill="url(#sea-open)"/>
    </g>
    <g role="img" aria-label="Underwater photo of a diver beside coral">
      <rect x="1240" y="602" width="149" height="105" fill="url(#sea-divers)"/>
    </g>
    <g role="img" aria-label="Photo of a sea turtle swimming over sand">
      <rect x="1389" y="602" width="296" height="105" fill="url(#sea-open)"/>
    </g>
  </g>

  <!-- Office building -->
  <g class="office-building">
    <polygon class="navy-fill" points="338,1097 863,855 1388,1097 1388,1608 338,1608"/>
    <polygon class="sky-fill" points="1027,931 1388,1097 1388,1608 775,1608"/>
    <polygon class="white-fill" points="687,952 863,870 1040,952 863,1033"/>
    <text class="brand-name" x="863" y="966" font-size="36" text-anchor="middle">KQ-Reef</text>
    <rect class="sky-fill" x="556" y="1158" width="181" height="248"/>
    <rect class="navy-fill" x="571" y="1173" width="151" height="218"/>
    <rect x="989" y="1158" width="181" height="248" fill="none" stroke="var(--white)" stroke-width="2"/>
    <rect class="navy-fill" x="1004" y="1173" width="151" height="218"/>
    <g class="partner-mark">
      <circle class="navy-fill" cx="940" cy="1358" r="28"/>
      <text class="brand-name" x="940" y="1408" font-size="28" text-anchor="middle">NEMO</text>
    </g>
    <rect class="orange-fill" x="1185" y="1159" width="174" height="44" rx="6"/>
    <text class="offer-title" x="1272" y="1186" font-size="29" text-anchor="middle" textLength="164">Unlimited Air</text>
    <text class="offer-sub" x="1272" y="1199" font-size="12" text-anchor="middle" textLength="150">No restrictions, dive freely!</text>
    <rect class="orange-fill" x="1185" y="1225" width="174" height="44" rx="6"/>
    <text class="offer-title" x="1270" y="1252" font-size="29" text-anchor="middle" textLength="136">Tank Cards</text>
    <text class="offer-sub" x="1272" y="1265" font-size="11" text-anchor="middle" textLength="164">Easy, flexible, and cost-effective.</text>
    <rect class="orange-fill" x="1185" y="1292" width="174" height="44" rx="6"/>
    <text class="offer-title" x="1266" y="1319" font-size="29" text-anchor="middle" textLength="154">Lowest Price</text>
    <text class="offer-sub" x="1262" y="1332" font-size="12" text-anchor="middle" textLength="130">Best deal on the island!</text>
    <rect class="orange-fill" x="1185" y="1358" width="174" height="44" rx="6"/>
    <text class="offer-title" x="1271" y="1385" font-size="28" text-anchor="middle" textLength="164">NEMO Certified</text>
    <text class="offer-sub" x="1272" y="1398" font-size="9" text-anchor="middle" textLength="162">A globally recognized diving standard.</text>
    <g class="web-address">
      <circle class="globe" cx="1165" cy="1430" r="10" stroke="var(--navy)"/>
      <line x1="1155" y1="1430" x2="1175" y2="1430" stroke="var(--navy)" stroke-width="2"/>
      <ellipse class="globe" cx="1165" cy="1430" rx="4" ry="10" stroke="var(--navy)" stroke-width="2"/>
      <text class="web navy-fill" x="1184" y="1441" font-size="34">kq-reef.com</text>
    </g>
    <text class="headline on-navy" x="402" y="1480" font-size="58" textLength="362">ENJOY THE</text>
    <text class="headline" x="394" y="1533" font-size="58" textLength="380"><tspan class="on-navy">WATERS</tspan><tspan class="accent"> OF</tspan></text>
    <text class="headline accent" x="390" y="1585" font-size="58" textLength="308">BONAIRE</text>
    <g role="img" aria-label="Underwater photo of a sea turtle">
      <polygon points="835,1448 998,1448 998,1608 775,1608" fill="url(#sea-turtle)"/>
    </g>
    <g role="img" aria-label="Underwater photo of divers over coral">
      <rect x="998" y="1448" width="186" height="160" fill="url(#sea-divers)"/>
    </g>
    <g role="img" aria-label="Photo of a queen angelfish on the reef">
      <rect x="1184" y="1448" width="204" height="160" fill="url(#sea-angelfish)"/>
    </g>
  </g>

  <!-- Pickup truck tailgate sticker -->
  <g class="tailgate-sticker">
    <rect class="navy-fill" x="514" y="1822" width="656" height="233"/>
    <polygon class="sky-fill" points="938,1822 1170,1822 1170,2055 835,2055"/>
    <g role="img" aria-label="Underwater photo of a sea turtle">
      <polygon points="840,1822 938,1822 906,1895 809,1895" fill="url(#sea-turtle)"/>
    </g>
    <g role="img" aria-label="Photo of a queen angelfish on the reef">
      <polygon points="809,1895 906,1895 869,1977 773,1977" fill="url(#sea-angelfish)"/>
    </g>
    <g role="img" aria-label="Underwater photo of divers over coral">
      <polygon points="773,1977 869,1977 835,2055 740,2055" fill="url(#sea-divers)"/>
    </g>
    <polygon class="white-fill" points="556,1822 672,1822 672,1905 614,1930 556,1905"/>
    <text class="brand-name" x="614" y="1880" font-size="24" text-anchor="middle">KQ-Reef</text>
    <g class="partner-mark">
      <circle class="navy-fill" cx="1120" cy="1842" r="15"/>
      <text class="brand-name" x="1120" y="1873" font-size="15" text-anchor="middle">NEMO</text>
    </g>
    <text class="headline on-navy" x="540" y="1966" font-size="34" textLength="214">ENJOY THE</text>
    <text class="headline" x="534" y="1998" font-size="34" textLength="226"><tspan class="on-navy">WATERS</tspan><tspan class="accent"> OF</tspan></text>
    <text class="headline accent" x="531" y="2028" font-size="34" textLength="184">BONAIRE</text>
    <rect class="orange-fill" x="931" y="1884" width="207" height="53" rx="8"/>
    <text class="offer-title" x="1034" y="1917" font-size="36" text-anchor="middle" textLength="196">Unlimited Air</text>
    <text class="offer-sub" x="1034" y="1932" font-size="14" text-anchor="middle" textLength="178">No restrictions, dive freely!</text>
    <rect class="orange-fill" x="931" y="1954" width="207" height="53" rx="8"/>
    <text class="offer-title" x="1032" y="1987" font-size="36" text-anchor="middle" textLength="162">Tank Cards</text>
    <text class="offer-sub" x="1034" y="2001" font-size="13" text-anchor="middle" textLength="196">Easy, flexible, and cost-effective.</text>
    <g class="web-address">
      <circle class="globe" cx="901" cy="2031" r="12" stroke="var(--navy)"/>
      <line x1="889" y1="2031" x2="913" y2="2031" stroke="var(--navy)" stroke-width="2"/>
      <ellipse class="globe" cx="901" cy="2031" rx="5" ry="12" stroke="var(--navy)" stroke-width="2"/>
      <text class="web navy-fill" x="921" y="2044" font-size="38" textLength="216">kq-reef.com</text>
    </g>
  </g>
</svg>
</body>
</html>
```